Top New England Restaurant Needs Website Redesign

We currently have a website, rmsbistro.com, but would like to redesign it. We are a casual upscale restaurant specializing in breakfast and lunch. We are one of the top rated restaurants in all of New England and would like our site to look like it as well. We'd love to have a blog/news section that will be updated weekly or so, as well as an email capture feature on the page.

The site will mostly be static, with lots of pictures (I'll take them and provide). The only part of the site that will get updated regularly is the blog and/or news (could be the same page).

Some restaurant websites I like are: www.corvintable.com, www.brassandoat.com,

Target Market(s)

Foodies, RM's Bistro customers,

Industry/Entity Type

Restaurant

Logo Text

RM's Bistro

Font styles to use
Sans Serif

Requirements
Must have
• Friendloop Like Box, Dinetip Box, Email capture, Blog/News, About Us page, Contact page

```html
<!DOCTYPE html>
<html lang="en">
<head>
<meta charset="utf-8">
<title>RM's Bistro</title>
<link href="https://fonts.googleapis.com/css2?family=Fira+Sans:ital,wght@0,400;0,500;0,600;1,400&family=Graduate&family=Yellowtail&family=Alfa+Slab+One&display=swap" rel="stylesheet">
<style>
:root{
  --ink:#1d1d20;
  --hero:#1b1b1d;
  --cream:#f5f5e9;
  --text:#555;
  --orange:#f05a28;
  --blog:#e8794a;
  --lime:#c9d52f;
  --gold:#dca33a;
  --footer:#2b2b30;
  --footer-line:#3b3b41;
  --muted:#9a9aa0;
  --dinetip:#c41200;
  --star:#f26322;
}
*{box-sizing:border-box;margin:0;padding:0}
html,body{width:1200px;height:2655px;overflow:hidden}
body{font-family:"Fira Sans",sans-serif;color:var(--text);background:#fff;position:relative}
.abs{position:absolute}
h2{font-family:"Graduate",serif;font-weight:400;color:var(--ink);font-size:27px;letter-spacing:1px}

/* hero */
.hero{left:0;top:0;width:1200px;height:717px;background:radial-gradient(ellipse at 70% 45%,#333336 0%,#1e1e20 55%,#141415 100%)}
.logo{left:78px;top:34px;color:#fff;font-size:34px;font-weight:500}
.nav{right:80px;top:48px;display:flex;gap:31px;list-style:none}
.nav li{color:#fff;font-size:13px;font-weight:500;letter-spacing:.3px}
.intro{left:105px;top:308px;color:#e4e4e4;font-size:24px}
.headline{left:105px;top:335px;color:var(--lime);font-family:"Yellowtail",cursive;font-size:110px;line-height:1.05;transform:rotate(-4deg);transform-origin:left center;white-space:nowrap}
.burger-word{left:243px;top:452px;color:var(--gold);font-family:"Alfa Slab One",serif;font-size:76px;letter-spacing:2px}
.hero-photo{left:560px;top:250px;width:560px;height:450px;border-radius:4px;background:linear-gradient(180deg,#c98a45 0%,#8f4f25 55%,#3a2012 100%)}

/* about */
.about{left:0;top:717px;width:1200px;height:366px;background:var(--cream)}
.about h2{position:absolute;left:74px;top:56px}
.about p{position:absolute;left:74px;top:106px;width:670px;font-size:14.5px;line-height:24.5px}
.link{color:var(--orange);font-style:italic;font-size:14px;display:flex;align-items:center;gap:9px}
.about .link{position:absolute;left:74px;top:292px}
.dot{width:13px;height:13px;border-radius:50%;background:var(--orange);display:inline-block}
.chef-photo{left:793px;top:58px;width:333px;height:252px;background:linear-gradient(160deg,#d9c8a6,#b7a98c 50%,#e8e4dc)}
.chef-label{left:858px;top:293px;width:202px;height:33px;background:#000;color:#fff;font-size:14px;display:flex;align-items:center;justify-content:center}

/* features */
.feature{top:1083px;width:600px;height:360px;padding:60px 74px 0 74px;color:#f2f2f2}
.feature h2{color:#fff;margin-bottom:18px}
.feature p{font-size:14.3px;line-height:24px;width:460px}
.menu-panel{left:0;background:linear-gradient(135deg,#5a4770,#3c2b52 60%,#2f2240)}
.coffee-panel{left:600px;background:linear-gradient(135deg,#8a3a1d,#6b2a16 55%,#4c1d10)}
.btn{display:inline-flex;align-items:center;gap:8px;background:var(--orange);color:#fff;font-size:14px;height:32px;padding:0 14px;margin-top:20px;border-radius:2px}
.btn .dot{background:#fff;width:11px;height:11px}

/* social */
.social h2{position:absolute;top:1492px}
.fl-box{left:74px;top:1547px;width:510px;height:286px;border:1px solid #ddd;background:#fafafa}
.fl-cover{left:0;top:0;width:508px;height:108px;background:linear-gradient(180deg,#bfd4e0,#e3ebef 60%,#f2f2f2)}
.fl-name{left:14px;top:12px;display:flex;gap:8px;align-items:center;font-size:14px;color:#fff;font-weight:600}
.fl-name span.sq{width:40px;height:40px;background:#7fb2cf;border:2px solid #fff}
.fl-btn{font-size:11px;background:#fff;border:1px solid #ccc;padding:3px 8px;color:#444}
.fl-badge{left:213px;top:20px;width:56px;height:74px;background:#d32f2f}
.fl-faces{left:14px;top:128px;width:480px;height:140px;background:#fff;border:1px solid #e2e2e2;padding:8px}
.fl-faces p{font-size:10.5px;color:#777;margin-bottom:6px}
.faces{display:grid;grid-template-columns:repeat(14,1fr);gap:4px}
.faces i{display:block;height:26px;background:linear-gradient(135deg,#a99a86,#6f7a86)}
.dt-bar{left:614px;top:1545px;width:512px;height:52px;background:var(--dinetip);color:#fff;font-size:26px;font-weight:600;display:flex;align-items:center;justify-content:center}
.dt-item{left:632px;width:480px;display:flex;gap:20px}
.dt-thumb{width:54px;height:54px;background:linear-gradient(135deg,#8c7b62,#c7b79c);flex:none}
.dt-item h4{font-size:12px;font-weight:400;color:#444}
.stars{display:flex;align-items:center;gap:2px;margin:3px 0;font-size:11px;color:#777}
.stars b{width:13px;height:13px;background:var(--star);display:inline-block}
.stars b.off{background:#ccc}
.dt-item p{font-size:12.5px;color:#333}

/* blog */
.blog{left:0;top:1890px;width:1200px;height:354px;background:var(--blog)}
.blog h2{position:absolute;left:0;width:1200px;top:50px;text-align:center;color:#fff;font-size:25px}
.post{top:2024px;width:340px;color:#fff}
.post h3{font-size:16.5px;font-weight:500;margin-bottom:4px;white-space:nowrap}
.post .meta{font-size:11px;padding-bottom:12px;border-bottom:1px solid rgba(255,255,255,.3)}
.post .body{display:flex;gap:32px;margin-top:12px}
.post .thumb{width:148px;height:90px;flex:none}
.post .txt{font-size:12.5px;line-height:20px}
.post .txt em{display:block;margin-top:6px;font-size:12.5px}

/* footer */
.footer{left:0;top:2244px;width:1200px;height:411px;background:var(--footer)}
.foot-title{color:#fff;font-size:15px;font-weight:500}
.hours{left:74px;top:2276px;font-size:12.5px;color:var(--muted);line-height:26px}
.vline{left:377px;top:2244px;width:1px;height:142px;background:var(--footer-line)}
.hline{left:0;top:2386px;width:1200px;height:1px;background:var(--footer-line)}
.hline2{left:0;top:2590px;width:1200px;height:1px;background:var(--footer-line)}
.sub{left:434px;top:2276px}
.field{top:2318px;height:35px;background:#fff;color:#555;font-size:12.5px;padding:0 13px;display:flex;align-items:center}
.sub-btn{left:959px;top:2318px;width:107px;height:35px;background:var(--orange);color:#fff;font-size:12px;display:flex;align-items:center;justify-content:center;font-weight:500}
.map{left:74px;top:2420px;width:305px;height:138px;background:linear-gradient(135deg,#e9e7e2,#d6d3cc)}
.contact{left:434px;top:2412px;font-size:12.5px;color:var(--muted);line-height:19px}
.stay{left:704px;top:2412px}
.soc{display:flex;align-items:center;gap:14px;font-size:12.5px;color:var(--muted)}
.soc i{width:26px;height:26px;display:inline-block}
.copy{left:0;width:1200px;top:2614px;text-align:center;font-size:12px;color:var(--muted)}
</style>
</head>
<body>

<header class="abs hero">
  <svg class="abs" style="left:0;top:0" width="1200" height="717" aria-hidden="true">
    <circle cx="930" cy="560" r="440" fill="none" stroke="#3a3a3d" stroke-width="5"/>
  </svg>
  <div class="abs hero-photo" role="img" aria-label="Photo of the featured burger on a dark background"></div>
  <div class="abs logo">RM's Bistro</div>
  <ul class="abs nav">
    <li>HOME</li><li>ABOUT US</li><li>MENU</li><li>OUR COFFEE</li><li>GALLERY</li><li>NEWS</li><li>CONTACT</li>
  </ul>
  <div class="abs intro">Introducing The</div>
  <div class="abs headline">Grand Bite</div>
  <div class="abs burger-word">BURGER</div>
</header>

<section class="abs about">
  <h2>ABOUT US</h2>
  <p>RM's Bistro is committed to superior food quality and cultivating a pleasurable and welcoming dining experience, akin to enjoying a home-cooked meal. We are truly excited to bring a fresh, new restaurant for breakfast and lunch to the City of Harbors. From the warm welcome our guests will receive as they walk through our doors, through to the last bite of one of our savory dishes, we plan to take the dining experience you'd find in a critically acclaimed restaurant in Boston, and bring to the South Shore.</p>
  <div class="link"><span class="dot"></span>Read More About Our Company</div>
  <div class="abs chef-photo" role="img" aria-label="Portrait of the owner and chef in a white chef's hat"></div>
  <div class="abs chef-label">Owner/Chef Ray Moreno</div>
</section>

<section class="abs feature menu-panel" role="img" aria-label="Overhead photo of breakfast dishes on a table, tinted purple">
  <h2>OUR MENU</h2>
  <p>RM's Bistro features a smaller menu designed to take advantage of seasonal menu items that can be switched out occasionally, thus ensuring only the best dishes make the cut. Try our famed Sunrise Benedict or our customer-named Milo Burger topped with a fried egg and chipotle barbeque sauce and you'll leave wanting to come back for more.</p>
  <span class="btn"><span class="dot"></span>Explore Our Menu</span>
</section>
<section class="abs feature coffee-panel" role="img" aria-label="Photo of coffee being poured into a cup, tinted warm red">
  <h2>OUR COFFEE</h2>
  <p>Coffee is, without a doubt, one of the best parts of a morning meal.  Some people can't even go 13 seconds without a sip of a delicious cup of freshly brewed coffee, java, joe, liquid energy, morning thunder, daily grind, jet fuel, wakey wakey juice (OK, I may or may not have made that last one up).  No sooner than we signed all the papers for RM's Bistro.</p>
  <span class="btn"><span class="dot"></span>Read More Coffee</span>
</section>

<section class="social">
  <h2 style="left:74px">LIKE US ON FRIENDLOOP</h2>
  <h2 style="left:614px">LIKE US ON DINETIP</h2>

  <div class="abs fl-box">
    <div class="abs fl-cover" role="img" aria-label="Restaurant cover photo"></div>
    <div class="abs fl-name"><span class="sq"></span><span>RM's Bistro<br><small style="font-weight:400;font-size:10px">3,151 likes</small></span></div>
    <div class="abs fl-badge"></div>
    <div class="abs fl-btn" style="left:12px;top:84px">Like Page</div>
    <div class="abs fl-btn" style="left:444px;top:84px">Share</div>
    <div class="abs fl-faces">
      <p>Be the first of your friends to like this</p>
      <div class="faces" role="img" aria-label="Grid of follower profile photos">
        <i></i><i></i><i></i><i></i><i></i><i></i><i></i><i></i><i></i><i></i><i></i><i></i><i></i><i></i>
        <i></i><i></i><i></i><i></i><i></i><i></i><i></i><i></i><i></i><i></i><i></i><i></i><i></i><i></i>
        <i></i><i></i><i></i><i></i><i></i><i></i><i></i><i></i><i></i><i></i><i></i><i></i><i></i><i></i>
      </div>
    </div>
  </div>

  <div class="abs dt-bar">Dinetip</div>
  <div class="abs dt-item" style="top:1616px"><div class="dt-thumb" role="img" aria-label="Dish photo"></div><div><h4>RM's Bistro</h4><div class="stars"><b></b><b></b><b></b><b></b><b class="off"></b>&nbsp;68 reviews</div><p>Veggie scrambler and home fries come highly recommended!</p></div></div>
  <div class="abs dt-item" style="top:1690px"><div class="dt-thumb" role="img" aria-label="Dining room photo"></div><div><h4>RM's Bistro</h4><div class="stars"><b></b><b></b><b></b><b></b><b class="off"></b>&nbsp;68 reviews</div><p>Veggie scrambler and home fries come highly recommended!</p></div></div>
  <div class="abs dt-item" style="top:1765px"><div class="dt-thumb" role="img" aria-label="Storefront photo"></div><div><h4>RM's Bistro</h4><div class="stars"><b></b><b></b><b></b><b></b><b class="off"></b>&nbsp;68 reviews</div><p>Veggie scrambler and home fries come highly recommended!</p></div></div>
</section>

<section class="abs blog">
  <h2>LATEST BLOG POSTS</h2>
</section>
<article class="abs post" style="left:83px">
  <h3>Enter as Strangers, Leave as Friends</h3>
  <div class="meta">By Marcus | On February 22, 2015 | 0 Comments</div>
  <div class="body"><div class="thumb" role="img" aria-label="Chef plating food in the kitchen" style="background:linear-gradient(135deg,#d8d8d8,#8a8a8a)"></div><div class="txt">Working in the hospitality business for as long as my father and I have...<em>Read More »</em></div></div>
</article>
<article class="abs post" style="left:443px">
  <h3>Chef Ray on 'What's Cooking?' (Channel 9)</h3>
  <div class="meta">By Marcus | On January 30, 2015 | 0 Comments</div>
  <div class="body"><div class="thumb" role="img" aria-label="Thank-you sign from the television feature" style="background:linear-gradient(135deg,#3f5a2a,#7a9a3a)"></div><div class="txt">We were ecstatic when we got the email from the Executive Producer...<em>Read More »</em></div></div>
</article>
<article class="abs post" style="left:804px">
  <h3>RM's Teams Up With Hope Circle</h3>
  <div class="meta">By Marcus | On May 24, 2014 | No Comments</div>
  <div class="body"><div class="thumb" role="img" aria-label="Glass of iced drink on a counter" style="background:linear-gradient(135deg,#3a2f2a,#e8e4dc)"></div><div class="txt">We are thrilled to announce a new partnership...<em>Read More »</em></div></div>
</article>

<footer class="abs footer"></footer>
<div class="abs vline"></div>
<div class="abs hline"></div>
<div class="abs hline2"></div>
<div class="abs hours"><h4 class="foot-title" style="margin-bottom:10px">Hours</h4>Tuesday to Sunday&nbsp; :&nbsp; 07:00 AM — 03:00 PM<br>Monday : Closed</div>
<div class="abs sub"><h4 class="foot-title">Subscribe Newsletter</h4></div>
<div class="abs field" style="left:434px;width:256px">Name</div>
<div class="abs field" style="left:693px;width:257px">Email</div>
<div class="abs sub-btn">SUBSCRIBE</div>
<div class="abs map" role="img" aria-label="Street map showing the restaurant location"></div>
<div class="abs contact"><h4 class="foot-title" style="margin-bottom:16px">Contact Information</h4>RM's Bistro<br>418 Harbor Ave.<br>Easton, MA 02375<br><br>Phone: 508-555-0147</div>
<div class="abs stay">
  <h4 class="foot-title" style="margin-bottom:22px">Stay Conneted</h4>
  <div style="display:grid;grid-template-columns:204px 200px;row-gap:28px">
    <div class="soc"><i style="background:#3b5998"></i>Follow Us Friendloop</div>
    <div class="soc"><i style="background:#1da1f2"></i>Follow Us Chirpline</div>
    <div class="soc"><i style="background:#c41200"></i>Follow Us Dinetip</div>
    <div class="soc"><i style="background:#3f729b"></i>Follow Us Snapframe</div>
  </div>
</div>
<div class="abs copy">Copyright ©2016 RM's Bistro. All Rights Reserved</div>

</body>
</html>
```